IT support company needs Banner Ad for the top of their quote layout template

We need a banner Ad for the top of our for quote layout template so it is sent out on all our quotes

The banner size must be 827 x 100 pixels - anything larger than 60 KB can cause upload time issues

We have attached our logo and examples of the quote page to see how it looks in the context of the whole page.

Essential elements of the banner
- Must have our logo but this can be changed to be different colours if it makes the design work better i.e. Tidal Grove could be all in white

Colours
- Can use all of our standard colours - Orange, Black, Grey and White

Images
- As a premium IT support company we deal with people and technology so would like to see both of these Incorporated into the banner i.e. people using technology These images could be watermarked or one colour effect.

Look and Feel
- Professional, friendly, people, technology, premium

Target Market
Small business owners and managers

Industry/Entity Type

It Company

```html
<!DOCTYPE html>
<html lang="nl">
<head>
<meta charset="utf-8">
<title>Offerte HB-000280</title>
<link href="https://fonts.googleapis.com/css2?family=Source+Sans+3:wght@400;600;700&family=Montserrat:wght@700;800&display=swap" rel="stylesheet">
<style>
:root{
  --orange:#f26522;
  --orange-dark:#d9531a;
  --peach:#fde4d8;
  --ink:#111;
  --grey:#555;
  --night:#2a211d;
  --paper:#fff;
}
*{box-sizing:border-box;margin:0;padding:0}
html,body{width:1200px;height:1200px;overflow:hidden;background:#fff}
body{position:relative;font-family:"Source Sans 3",sans-serif;color:var(--ink)}
.page{position:absolute;left:293px;top:166px;width:767px;height:1086px;transform:scale(.8);transform-origin:0 0;background:var(--paper);outline:1px solid #ddd}
.abs{position:absolute;white-space:nowrap}

.banner{position:absolute;left:0;top:0;width:767px;height:94px;background:linear-gradient(100deg,var(--orange) 0%,#ee5a1c 40%,#f47a36 75%,var(--orange-dark) 100%);overflow:hidden}
.banner-photo{position:absolute;inset:0;background:linear-gradient(160deg,#4a3a32,var(--night) 60%,#1a1411);clip-path:polygon(199px 0,504px 0,442px 94px,139px 94px)}
.brand{left:23px;top:36px;font-family:"Montserrat",sans-serif;font-weight:700;font-size:16px;color:#fff;letter-spacing:.3px}
.headline{left:225px;top:22px;font-family:"Montserrat",sans-serif;font-weight:800;font-size:19px;line-height:22px;color:#fff;letter-spacing:1px}
.headline span{display:block;color:var(--orange);padding-left:3px}
.perks{left:515px;top:18px;list-style:none;font-family:"Montserrat",sans-serif;font-weight:700;font-size:12.5px;line-height:21.5px;color:#fff;letter-spacing:.4px}
.perks li{display:flex;align-items:center;gap:6px}
.banner-rule{position:absolute;left:0;top:96px;width:767px;height:6px;background:var(--orange)}

.doc-title{left:25px;top:149px;font-size:18px;font-weight:600}
.photo{position:absolute;left:24px;top:186px;width:91px;height:120px;background:linear-gradient(180deg,#9a9a9a,#4d4d4d)}
.party{position:absolute;top:183px;font-size:11.5px;line-height:16px}
.party h3{font-size:14px;font-weight:400;color:var(--orange);margin-bottom:5px}
.party b{font-weight:700}
.gap{height:15px}
.rule{position:absolute;left:24px;top:316px;width:718px;height:2px;background:var(--orange)}

.section-title{left:25px;font-size:16px;font-weight:600}
table{position:absolute;left:24px;width:718px;border-collapse:collapse;border:1.5px solid var(--ink);font-size:11.5px}
th{background:var(--orange);color:var(--ink);font-weight:400;height:22px;padding:0 5px;text-align:left;border-bottom:1.5px solid var(--ink)}
td{height:24px;padding:0 5px}
.num{text-align:right;border-left:1.5px solid var(--ink);width:101px}
tr.alt td{background:var(--peach)}
.sum{position:absolute;right:30px;font-size:11.5px;display:flex;gap:0}
.sum .label{color:var(--orange);text-align:right;width:400px;padding-right:47px}
.sum .value{font-weight:700;text-align:right;width:60px}

.notice{left:25px;top:876px;font-size:11.5px}
.sign-line{position:absolute;top:942px;height:1px;background:var(--ink)}
.sign-label{top:944px;font-size:11.5px}

.footer-rule{position:absolute;left:0;top:1036px;width:767px;height:6px;background:var(--orange)}
.footer{position:absolute;left:0;top:1047px;width:767px;height:39px;background:var(--orange);display:flex;justify-content:space-between;align-items:center;padding:0 26px 0 25px;font-size:11.5px}
</style>
</head>
<body>
<div class="page">
  <header class="banner">
    <div class="banner-photo" role="img" aria-label="Dark close-up photo of a laptop keyboard"></div>
    <div class="abs brand">Tidal Grove</div>
    <div class="abs headline">The East Anglia<span>IT Experts</span></div>
    <ul class="abs perks">
      <li><svg width="12" height="10" viewBox="0 0 12 10"><path d="M1 5l3.5 3.5L11 1.5" fill="none" stroke="#fff" stroke-width="2.2"/></svg>Proactive Care</li>
      <li><svg width="12" height="10" viewBox="0 0 12 10"><path d="M1 5l3.5 3.5L11 1.5" fill="none" stroke="#fff" stroke-width="2.2"/></svg>Round the Clock Maintenance</li>
      <li><svg width="12" height="10" viewBox="0 0 12 10"><path d="M1 5l3.5 3.5L11 1.5" fill="none" stroke="#fff" stroke-width="2.2"/></svg>Live Help Desk Support</li>
    </ul>
  </header>
  <div class="banner-rule"></div>

  <h1 class="abs doc-title">Standard MSP&nbsp; #2</h1>
  <div class="photo" role="img" aria-label="Portrait photo of the account manager"></div>

  <div class="party" style="left:125px">
    <h3>Opgesteld door:</h3>
    <b>Harlow Byrne Ltd</b><br>Harlow Byrne<br><div class="gap"></div>Fax<br>harlow.byrne@ferncastle.com
  </div>
  <div class="party" style="left:334px">
    <h3>Opgesteld voor:</h3>
    <b>Copper Ridge</b><br>1720 Alder Ln.<br>Millbrook,&nbsp;&nbsp; 40821<br>Rosa Whitfield<br>r.whitfield@brightmoss.co.uk
  </div>
  <div class="party" style="left:581px">
    <h3>Gegevens Offerte:</h3>
    <b>Offerte #: HB-000280</b><br>Versie: 1<br>Leverdatum: 14/11/2017<br>Vervaldatum: 31/12/2017
  </div>
  <div class="rule"></div>

  <h2 class="abs section-title" style="top:336px">Overzicht Offerte</h2>
  <table style="top:361px">
    <tr><th>Beschrijving</th><th class="num">Bedrag</th></tr>
    <tr><td>Initial Investment</td><td class="num">$800.00</td></tr>
  </table>
  <div class="sum" style="top:416px"><span class="label">Subtotaal:</span><span class="value">$800.00</span></div>
  <div class="sum" style="top:439px"><span class="label">VAT:</span><span class="value">$160.00</span></div>
  <div class="sum" style="top:462px"><span class="label">Totaal:</span><span class="value">$960.00</span></div>

  <h2 class="abs section-title" style="top:500px">Overzicht Terugkerende Kosten</h2>
  <table style="top:524px">
    <tr><th>Beschrijving</th><th class="num">Bedrag</th></tr>
    <tr><td>Monitoring</td><td class="num">$375.00</td></tr>
    <tr class="alt"><td>Support</td><td class="num">$65.00</td></tr>
    <tr><td>Fixed Hours</td><td class="num">$850.00</td></tr>
  </table>
  <div class="sum" style="top:627px"><span class="label">Terugkerende totaal:</span><span class="value">$1,290.00</span></div>

  <h2 class="abs section-title" style="top:665px">*Optionele kosten</h2>
  <table style="top:689px">
    <tr><th>Beschrijving</th><th class="num">Recurring</th><th class="num">One-Time</th></tr>
    <tr><td>Monitoring</td><td class="num">$790.00</td><td class="num">$0.00</td></tr>
    <tr class="alt"><td>Support</td><td class="num">$185.00</td><td class="num">$0.00</td></tr>
    <tr><td>Fixed Hours</td><td class="num">$695.00</td><td class="num">$0.00</td></tr>
    <tr class="alt"><td>Add-on Services</td><td class="num">$850.00</td><td class="num">$0.00</td></tr>
  </table>
  <div class="sum" style="top:816px"><span class="label">Optionele terugkerend bedrag:</span><span class="value">$2,520.00</span></div>
  <div class="sum" style="top:839px"><span class="label">Optionele ongeplande Subtotaal:</span><span class="value">$.00</span></div>

  <p class="abs notice">Taxes, shipping, handling and other fees may apply.&nbsp; We reserve the right to cancel orders arising from pricing or other errors.</p>

  <div class="sign-line" style="left:24px;width:430px"></div>
  <div class="abs sign-label" style="left:25px">Handtekening</div>
  <div class="sign-line" style="left:480px;width:170px"></div>
  <div class="abs sign-label" style="left:482px">Datum</div>

  <div class="footer-rule"></div>
  <footer class="footer"><span>Offerte #HB-000280 v1</span><span>Pagina 6 Van 7</span></footer>
</div>
</body>
</html>
```